WP website design (Vorne)

We need a wordpress design for an established auction and real estate company based in Kentucky. The winning design will incorporate a professional color scheme with company logo in a clean layout with specified widgets. The design needs to consider that this will be developed on a responsive theme. Colors will complement the colors in the logo.

Industry/Entity Type

Real Estate

Font styles to use
Sans Serif

Requirements
Must have
• - Navigation:
1) Home 2) Auctions 3) Real Estate Listings 4) Our Services 5) Why Auctions 6) About Us 7) Past Auctions 8) Contact Us

Homeage will have slideshow, please use stock real estate image as the initial slide. Homepage will have this content: "Martin Vorne Auctioneer Real Estate Broker

Buying or selling you can count on Martin Vorne Auctioneer to deliver a quality auction experience. We handle all the details from initial handshake to final payment. We are with you every step of the way giving our sellers the service and results they deserve. You only have one chance for a successful auction. Contact us today to see how our experience and know-how can work for you. We are confident that you will appreciate our higher standard of service."

Footer will have smaller company logo, and attached association logos and this contact info:
Phone: (270) 555-0148
Contacts: Martin Vorne
Email: martinvorne@mailbrook.example
Address: 482 Pellworth Lane • Bowling Green, KY 42917

Widgets:
1) email sign up 2) Social media (twitter, Youtube - can also be in header 3) News & Events Blog widget 4) testimonials blog 5) Featured Video widget
Nice to have
• Nice to Have:
- demonstrate the drop-down menu styling, e.g. under Auctions
-Upcoming Auctions
-Online Auctions
-Past Auctions

```html
<!DOCTYPE html>
<html lang="en">
<head>
<meta charset="utf-8">
<title>Martin Vorne Auctioneer Real Estate Broker</title>
<link rel="stylesheet" href="https://fonts.googleapis.com/css2?family=Mulish:ital,wght@0,400;0,600;0,700;1,400&family=Didact+Gothic&display=swap">
<style>
:root{
  --blue:#1f5fae;
  --blue-dark:#0f3f86;
  --navy:#14286b;
  --yellow:#f4c51c;
  --orange:#eea012;
  --text:#333;
  --muted:#555;
  --link:#1f5fae;
  --line:#d9d9d9;
  --panel:#f3f3f3;
}
*{box-sizing:border-box;margin:0;padding:0}
html,body{width:673px;height:1200px;overflow:hidden;background:#fff}
body{position:relative;font-family:"Mulish",sans-serif;color:var(--text)}
.abs{position:absolute}

.site-header{position:absolute;left:0;top:0;width:673px;height:90px;background:linear-gradient(#fff,#f2f2f2)}
.brand{position:absolute;left:64px;top:30px;display:flex;align-items:center;gap:7px}
.brand-mark{width:22px;height:22px;background:var(--blue)}
.brand-name{font-size:17px;font-weight:700;color:var(--blue);letter-spacing:.2px}
.connect{position:absolute;left:546px;top:47px;font-size:8px;color:#444}
.social{position:absolute;top:63px;width:15px;height:15px;border-radius:2px}

.main-nav{position:absolute;left:0;top:90px;width:673px;height:32px;background:linear-gradient(#3a7fd0,var(--blue) 55%,#1a55a0)}
.main-nav a{position:absolute;top:0;height:32px;line-height:32px;font-size:9.5px;color:#fff;text-decoration:none;font-weight:600;padding:0 7px;border-left:1px solid rgba(255,255,255,.18)}
.main-nav a.active{background:var(--blue-dark)}
.main-nav a.first{border-left:none}
.dropdown{position:absolute;left:111px;top:122px;width:105px;height:62px;background:var(--blue-dark)}
.dropdown a{display:block;height:17px;line-height:17px;font-size:7.5px;color:#fff;text-decoration:none;padding-left:18px;border-bottom:1px solid rgba(255,255,255,.12);position:relative;margin-top:1px}
.dropdown a::before{content:"›";position:absolute;left:10px;color:#8fb3e6}

.hero{position:absolute;left:0;top:122px;width:673px;height:246px;background:linear-gradient(170deg,#f6d21e 0%,#f3b61b 45%,#ec9a12 100%)}
.hero-photo{position:absolute;left:300px;top:0;width:373px;height:246px;background:linear-gradient(90deg,rgba(243,190,27,0) 0%,rgba(230,225,205,.85) 30%,#e9e6dc 60%,#d9dbd0 80%,#b9c4a4 100%)}
.hero h1{position:absolute;left:65px;top:70px;font-family:"Didact Gothic",sans-serif;font-weight:400;font-size:21px;line-height:22px;color:#2b2b2b}
.hero h1 span{display:block;font-size:17.5px}
.hero p{position:absolute;left:65px;top:120px;width:230px;font-size:7px;line-height:12px;color:#6b4a0d}
.dots{position:absolute;left:65px;top:152px;display:flex;gap:3px}
.dots i{width:6px;height:6px;border-radius:50%;background:#fff}

.section-title{position:absolute;left:64px;top:384px;font-family:"Didact Gothic",sans-serif;font-size:13.5px;color:#222}
.auction{position:absolute;left:62px;width:366px;height:134px}
.auction .thumb{position:absolute;left:0;top:0;width:124px;height:108px}
.auction h3{position:absolute;left:136px;top:3px;font-family:"Didact Gothic",sans-serif;font-weight:400;font-size:13.5px;color:var(--link);white-space:nowrap}
.auction .desc{position:absolute;left:136px;top:23px;width:230px;font-size:6.8px;line-height:11.5px;color:#555}
.auction .desc b{color:var(--navy);font-weight:600}
.auction .mode{position:absolute;left:136px;top:61px;font-size:8px;font-weight:600;color:#222}
.date{position:absolute;top:79px;width:32px;height:28px;border-radius:2px;color:#fff;font-size:8px;line-height:10px;text-align:center;padding-top:4px}
.date.start{left:136px;background:linear-gradient(#2d4ea1,var(--navy))}
.date.end{left:194px;background:linear-gradient(var(--yellow),var(--orange))}
.date-to{position:absolute;left:177px;top:88px;font-size:9px;color:#444}
.auction .rule{position:absolute;left:0;top:121px;width:366px;height:1px;background:var(--line)}

.widget{position:absolute;left:444px;width:164px;border:1px solid #ddd;border-radius:2px;background:#fff}
.video{top:385px;height:117px;background:linear-gradient(135deg,#cfdcea,#a8bcd3 60%,#8fa7c4)}
.video .play{position:absolute;left:70px;top:40px;width:22px;height:22px;border-radius:50%;background:#222;border:1.5px solid #fff}
.video .play::after{content:"";position:absolute;left:8px;top:5px;border-left:8px solid #fff;border-top:5px solid transparent;border-bottom:5px solid transparent}
.video .caption{position:absolute;left:0;bottom:0;width:100%;height:26px;background:rgba(30,80,160,.9);color:#fff;font-family:"Didact Gothic",sans-serif;font-size:11px;line-height:26px;padding-left:11px}
.signup{top:509px;height:106px}
.signup .head{height:29px;background:linear-gradient(var(--yellow),var(--orange));color:#fff;font-family:"Didact Gothic",sans-serif;font-size:12px;line-height:29px;padding-left:13px;position:relative}
.signup .head svg{position:absolute;right:14px;top:7px}
.signup p{font-size:6.8px;color:#444;margin:12px 0 0 13px}
.signup .field{margin:5px 0 0 13px;width:138px;height:17px;border:1px solid #ccc;background:#f7f7f7;font-size:6.5px;color:#555;line-height:15px;padding-left:7px}
.signup .btn{margin:6px 0 0 13px;width:56px;height:17px;background:var(--navy);color:#fff;font-size:7px;font-weight:700;text-align:center;line-height:17px;border-radius:2px}
.panel-head{height:30px;background:linear-gradient(#fafafa,#ececec);border-bottom:1px solid #ddd;font-family:"Didact Gothic",sans-serif;font-size:12.5px;color:#333;line-height:30px;padding-left:14px}
.news{top:620px;height:213px}
.news .post{margin:10px 0 0 16px;width:135px}
.news .post h4{font-size:7.5px;font-weight:600;color:var(--navy)}
.news .post p{font-size:6.3px;line-height:10.5px;color:#444;margin-top:2px}
.news .post a{font-size:6.3px;color:var(--link);text-decoration:none}
.reviews{top:839px;height:203px}
.reviews blockquote{margin:14px 0 0 14px;width:130px;font-size:6.2px;line-height:10.5px;font-style:italic;color:#444;position:relative;padding-left:9px}
.reviews blockquote::before{content:"“";position:absolute;left:0;top:-3px;font-size:13px;color:#aaa;font-style:normal}
.reviews cite{display:block;font-style:normal;font-weight:600;font-size:6.3px;color:#222;margin:6px 0 0 0}

.site-footer{position:absolute;left:0;top:1100px;width:673px;height:100px;border-top:1px solid #ddd;background:linear-gradient(#f3f3f3,#fff 40%)}
.badge{position:absolute;top:1126px;height:24px;background:#222}
.copyright{position:absolute;left:72px;top:1167px;font-size:6.8px;color:#555}
.contact{position:absolute;right:65px;top:1119px;text-align:right;font-size:7.5px;line-height:12.8px;color:#333}
</style>
</head>
<body>

<header class="site-header">
  <div class="brand"><span class="brand-mark"></span><span class="brand-name">Martin Vorne</span></div>
  <div class="connect">Get Connected</div>
  <span class="social" style="left:548px;background:#c4302b" role="img" aria-label="Video channel"></span>
  <span class="social" style="left:567px;background:#3b5998" role="img" aria-label="Social profile"></span>
  <span class="social" style="left:586px;background:#29a9e1" role="img" aria-label="Microblog profile"></span>
</header>

<nav class="main-nav">
  <a class="first" style="left:71px">Home</a>
  <a class="active" style="left:111px;width:53px">Auctions</a>
  <a style="left:164px">Real Estate Listings</a>
  <a style="left:264px">Our Services</a>
  <a style="left:333px">Why Auctions</a>
  <a style="left:409px">About Us</a>
  <a style="left:464px">Past Auctions</a>
  <a style="left:538px">Contact Us</a>
</nav>

<section class="hero">
  <div class="hero-photo" role="img" aria-label="Row of white suburban townhouses with picket fence"></div>
  <h1>Mauris nunc quam venenatis<span>Aliquam volutpat Quisque</span></h1>
  <p>Etiam est nunc venenatis in tristique eu imperdiet ac nisl Cum sociis natoque penatibus et magnis dis parturient</p>
  <div class="dots"><i></i><i></i><i></i><i></i></div>
</section>
<div class="dropdown">
  <a>Upcoming Auctions</a><a>Online Auctions</a><a>Past Auctions</a>
</div>

<h2 class="section-title">Upcoming Auctions</h2>

<article class="auction" style="top:412px">
  <div class="thumb" role="img" aria-label="Two-storey house on a green lawn" style="background:linear-gradient(#7fa7d6,#b9cde3 40%,#6f7e5f 60%,#5c8a2e)"></div>
  <h3>Nam eget lacus Aliquam</h3>
  <p class="desc">Maecenas at justo id velit placerat molestie Donec dictum lectus non odio Cras a ante vitae enim iaculis aliquam Mauris nunc quam<br><b>Location:</b> P.O. Box 40217 &nbsp;Millbrook, VA 24990</p>
  <div class="mode">Live On-Site Auction with Online Bidding</div>
  <div class="date start">08<br>MAY</div><span class="date-to">to</span><div class="date end">25<br>MAY</div>
  <div class="rule"></div>
</article>

<article class="auction" style="top:546px">
  <div class="thumb" role="img" aria-label="Brick family home with family seated on the lawn" style="background:linear-gradient(#9fbde0,#c9c2b4 35%,#9a8672 65%,#6f8f45)"></div>
  <h3>Vestibulum ligula augue bibendum</h3>
  <p class="desc">Maecenas at justo id velit placerat molestie Donec dictum lectus non odio Cras a ante vitae enim iaculis aliquam Mauris nunc quam<br><b>Location:</b> P.O. Box 40217 &nbsp;Millbrook, VA 24990</p>
  <div class="mode">Live On-Site Auction with Online Bidding</div>
  <div class="date start">08<br>MAY</div><span class="date-to">to</span><div class="date end">25<br>MAY</div>
  <div class="rule"></div>
</article>

<article class="auction" style="top:680px">
  <div class="thumb" role="img" aria-label="White colonial house with garden" style="background:linear-gradient(#6f9fd8,#e1e2dc 40%,#b9b6a8 60%,#4e7a2c)"></div>
  <h3>Cras a ante vitae enim</h3>
  <p class="desc">Maecenas at justo id velit placerat molestie Donec dictum lectus non odio Cras a ante vitae enim iaculis aliquam Mauris nunc quam<br><b>Location:</b> P.O. Box 40217 &nbsp;Millbrook, VA 24990</p>
  <div class="mode">Live On-Site Auction with Online Bidding</div>
  <div class="date start">08<br>MAY</div><span class="date-to">to</span><div class="date end">25<br>MAY</div>
  <div class="rule"></div>
</article>

<article class="auction" style="top:814px">
  <div class="thumb" role="img" aria-label="Bright entrance hallway with glass doors" style="background:linear-gradient(90deg,#c9bfb3,#efeae2 45%,#b8aea0)"></div>
  <h3>Etiam est nunc venenatis in tristique</h3>
  <p class="desc">Maecenas at justo id velit placerat molestie Donec dictum lectus non odio Cras a ante vitae enim iaculis aliquam Mauris nunc quam<br><b>Location:</b> P.O. Box 40217 &nbsp;Millbrook, VA 24990</p>
  <div class="mode">Live On-Site Auction with Online Bidding</div>
  <div class="date start">08<br>MAY</div><span class="date-to">to</span><div class="date end">25<br>MAY</div>
  <div class="rule"></div>
</article>

<article class="auction" style="top:948px">
  <div class="thumb" role="img" aria-label="Warmly lit living room with large windows" style="background:linear-gradient(90deg,#7a5a3c,#d9b27a 45%,#a98960 70%,#6f7f5a)"></div>
  <h3>Phasellus pellentesque aliquam enim</h3>
  <p class="desc">Maecenas at justo id velit placerat molestie Donec dictum lectus non odio Cras a ante vitae enim iaculis aliquam Mauris nunc quam<br><b>Location:</b> P.O. Box 40217 &nbsp;Millbrook, VA 24990</p>
  <div class="mode">Live On-Site Auction with Online Bidding</div>
  <div class="date start">08<br>MAY</div><span class="date-to">to</span><div class="date end">25<br>MAY</div>
</article>

<aside>
  <div class="widget video" role="img" aria-label="Featured video still of smiling business people">
    <span class="play"></span>
    <div class="caption">Featured Video</div>
  </div>

  <div class="widget signup">
    <div class="head">Email Sign Up
      <svg width="17" height="13" viewBox="0 0 17 13"><rect x="0.5" y="0.5" width="16" height="12" rx="1.5" fill="#fff"/><path d="M1 2l7.5 5.5L16 2" fill="none" stroke="#f0aa15" stroke-width="1.6"/></svg>
    </div>
    <p>Please sign up here for latest auctions.</p>
    <div class="field">Email address</div>
    <div class="btn">SIGN UP</div>
  </div>

  <div class="widget news">
    <div class="panel-head">News/Blog Post</div>
    <div class="post"><h4>25 April 2014</h4><p>Vestibulum ligula augue bibendum ac cumsan vestibulum comm</p><a>Learn More</a></div>
    <div class="post"><h4>18 April 2014</h4><p>Malesuada nec ultricies sit amet porttitor mattis enim In massa libero interdum nec interdum vel blandit sed nulla</p><a>Learn More</a></div>
    <div class="post"><h4>05 April 2014</h4><p>Vestibulum ligula augue bibendum accum-san vestibulum comm Vestibulum ligu</p><a>Learn More</a></div>
  </div>

  <div class="widget reviews">
    <div class="panel-head" style="background:#fff">What Customer Say</div>
    <blockquote>Ut ante enim dapibus malesuada fringilla eu condimentum quis tellus Aenean porttitor eros vel dolor Donec convallis pede venena-tis nibh Duis quam Nam eget lac<cite>By Author Name</cite></blockquote>
    <blockquote>Maecenas at justo id velit placerat molestie Donec dictum lectus non odio Cras a ante vitae enim iaculis aliquam Mauris nunc quam venenatis nec euismod sit amet eges-tas placerat est Pellentesque<cite>By Author Name</cite></blockquote>
  </div>
</aside>

<footer class="site-footer"></footer>
<span class="badge" style="left:70px;width:46px;border-radius:50%" role="img" aria-label="Association badge"></span>
<span class="badge" style="left:130px;width:24px" role="img" aria-label="Association badge"></span>
<span class="badge" style="left:170px;width:50px" role="img" aria-label="Association badge"></span>
<span class="badge" style="left:234px;width:38px;border-radius:12px" role="img" aria-label="Certification badge"></span>
<span class="badge" style="left:286px;width:22px" role="img" aria-label="Membership badge"></span>
<div class="copyright">© 2014 Company Name &nbsp;All right reserved &nbsp;Term of Use</div>
<div class="contact">
  Phone: (270) 555-0148<br>
  Contacts: Martin Vorne<br>
  Email: martinvorne@mailbrook.example<br>
  Address: 482 Pellworth Lane &nbsp;Bowling Green, KY 42917
</div>

</body>
</html>
```